Video blogger website.

I'm looking to build a video blogger website I want cool, unique design. The ability to add banners on top of page. I would like to use embedded videos from sources like ClipVerra etc with the ability to share on social media . If needed I can provide example sites upon request. Like / dislike button similar to ClipVerra and Video View counter .10-15 pages with the availability to add more pages as site grows. I want the overall outline of the site to be original, but I want banners and all functions all to be done in WordPress. But I don't want a completely WordPress website due to certain limitations. Please no cookie cutters!!

Target Market(s)

Music, Comedy teens to adults

Build

Coding

Coded - Design and coding required

Number of Pages Required

5+ page

Colors

Designer to choose colors to be used in the design.

Requirements
Should not have
• No log in

```html
<!DOCTYPE html>
<html lang="en">
<head>
<meta charset="utf-8">
<title>Fenno Reels</title>
<link rel="stylesheet" href="https://fonts.googleapis.com/css2?family=Roboto:wght@400;500&family=Open+Sans:wght@400;600&display=swap">
<style>
:root{
  --ink:#222;
  --text:#333;
  --muted:#555;
  --line:#e3e3e3;
  --hero-bg:#ececec;
  --white:#fff;
  --red:#d0282e;
  --red-dark:#b91f25;
  --icon:#2b2b2b;
}
*{box-sizing:border-box;margin:0;padding:0}
html,body{width:1200px;height:2736px;overflow:hidden}
body{background:var(--white);font-family:"Open Sans",Arial,sans-serif;color:var(--text);position:relative}
.wrap{width:1004px;margin:0 auto;position:relative}

/* header */
.site-header{height:95px;border-bottom:1px solid var(--line)}
.site-header .wrap{display:flex;align-items:center;height:95px}
.brand-name{font-family:"Open Sans",sans-serif;font-weight:600;font-size:34px;color:var(--ink);letter-spacing:-.5px}
.main-nav{margin-left:auto;display:flex;gap:41px;align-items:center}
.main-nav a{font-family:"Roboto",sans-serif;font-size:13px;color:var(--ink);text-decoration:none;letter-spacing:.4px}
.search-btn{width:36px;height:36px;background:#e2e2e2;display:flex;align-items:center;justify-content:center;margin-left:-12px}

/* hero */
.hero{background:var(--hero-bg);height:644px;padding-top:38px;border-bottom:1px solid #d8d8d8}
.hero .wrap{display:flex;gap:4px}
.feature{width:741px;background:var(--white);height:553px;box-shadow:0 1px 2px rgba(0,0,0,.1)}
.feature-media{height:374px;position:relative;background:linear-gradient(160deg,#69753f 0%,#8f9155 40%,#a7784a 70%,#3e2b22 100%)}
.feature-body{padding:20px 16px 0}
.feature-title{font-family:"Roboto",sans-serif;font-weight:400;font-size:17px;color:var(--ink)}
.channel{display:flex;gap:12px;margin-top:20px;align-items:flex-start}
.avatar{width:58px;height:50px;background:linear-gradient(135deg,#c9b3a4,#7c5a4a)}
.channel-name{font-size:13px;color:var(--ink);margin-top:2px}
.sub-row{display:flex;align-items:center;margin-top:6px}
.sub-btn{background:var(--red);color:var(--white);font-size:10.5px;font-weight:600;height:22px;display:flex;align-items:center;gap:5px;padding:0 7px;border-radius:2px}
.sub-btn .dot{width:9px;height:9px;background:var(--white);border-radius:50%}
.sub-count{border:1px solid #ccc;height:22px;padding:0 5px;font-size:10px;display:flex;align-items:center;margin-left:4px}
.action-bar{border-top:1px solid var(--line);margin-top:26px;height:40px;display:flex;align-items:center;padding:0 14px;font-size:11px;color:var(--muted);gap:28px}
.action-bar .stat{margin-left:auto}
.action-bar span{display:flex;align-items:center;gap:6px}
.side-list{width:259px;display:flex;flex-direction:column;gap:2px}
.side-item{height:109px;background:var(--white);display:flex;box-shadow:0 1px 2px rgba(0,0,0,.08)}
.side-thumb{width:120px;position:relative;flex:none}
.side-text{padding:10px 12px;font-size:13px;line-height:19px;color:var(--ink)}
.side-text .views{margin-top:8px;font-size:13px;color:var(--muted)}

.play{position:absolute;left:50%;top:50%;transform:translate(-50%,-50%)}

/* video sections */
.section-title{font-family:"Roboto",sans-serif;font-weight:400;font-size:31px;color:var(--ink);text-align:center}
.card-row{display:flex;gap:18px;margin-top:42px}
.card{width:237px;height:265px;background:var(--white);box-shadow:0 1px 3px rgba(0,0,0,.18)}
.card-media{height:171px;position:relative}
.card-desc{font-size:11px;line-height:17px;color:var(--text);padding:12px 11px 0}
.card-meta{display:flex;justify-content:space-between;font-size:11.5px;padding:10px 11px 0;color:var(--ink)}

/* popular */
.popular{position:absolute;left:0;top:2079px;width:1200px;height:475px;background:linear-gradient(180deg,var(--red) 0%,var(--red-dark) 100%)}
.popular-title{font-family:"Roboto",sans-serif;font-weight:400;font-size:28px;color:var(--white);text-align:center;margin-top:52px}
.post-row{display:flex;gap:25px;margin-top:30px}
.post{width:232px;text-align:center;color:var(--white)}
.post-media{height:228px;position:relative;border:1px solid rgba(255,255,255,.6)}
.tag{position:absolute;left:50%;bottom:-8px;transform:translateX(-50%);background:var(--white);color:var(--red);font-size:9px;font-weight:600;padding:3px 8px;letter-spacing:.5px}
.post-title{font-size:12px;line-height:18px;margin-top:20px;font-weight:600}
.post-meta{display:flex;justify-content:center;gap:20px;font-size:9px;margin-top:9px}
.post-meta span{display:flex;align-items:center;gap:5px}

/* footer */
.site-footer{position:absolute;left:0;top:2554px;width:1200px;height:182px;text-align:center}
.social{display:flex;justify-content:center;gap:14px;margin-top:46px}
.social-link{width:22px;height:22px;background:var(--icon);border-radius:4px;display:flex;align-items:center;justify-content:center}
.foot-nav{margin-top:14px;font-size:13px;color:var(--ink)}
.foot-nav a{color:var(--ink);text-decoration:none}
.foot-nav i{font-style:normal;margin:0 8px}
.copyright{font-size:11.5px;margin-top:10px;color:var(--ink)}
</style>
</head>
<body>

<header class="site-header">
  <div class="wrap">
    <div class="brand-name">Fenno Reels</div>
    <nav class="main-nav">
      <a href="#">HOME</a><a href="#">TRENDING</a><a href="#">ENTERTAINMENT</a><a href="#">VIDEOS</a><a href="#">SUBSCRIPTIONS</a><a href="#">CONTACTS</a>
      <span class="search-btn"><svg width="12" height="12" viewBox="0 0 12 12"><circle cx="5" cy="5" r="3.5" fill="none" stroke="#777" stroke-width="1.5"/><line x1="7.5" y1="7.5" x2="11" y2="11" stroke="#777" stroke-width="1.5"/></svg></span>
    </nav>
  </div>
</header>

<section class="hero">
  <div class="wrap">
    <article class="feature">
      <div class="feature-media" role="img" aria-label="Woman in a meadow at sunset releasing a heart balloon">
        <svg class="play" width="50" height="50" viewBox="0 0 50 50"><circle cx="25" cy="25" r="22" fill="none" stroke="#fff" stroke-width="3"/><path d="M20 15 L35 25 L20 35Z" fill="#fff"/></svg>
      </div>
      <div class="feature-body">
        <h1 class="feature-title">Nemo enim ipsam voluptatem quia voluptas sit</h1>
        <div class="channel">
          <div class="avatar" role="img" aria-label="Channel avatar"></div>
          <div>
            <div class="channel-name">Nemo enim ipsam</div>
            <div class="sub-row"><span class="sub-btn"><span class="dot"></span>ClipVerra Subscribe</span><span class="sub-count">10K</span></div>
          </div>
        </div>
      </div>
      <div class="action-bar">
        <span><svg width="10" height="10"><path d="M5 0v10M0 5h10" stroke="#555" stroke-width="1.6"/></svg>Add to</span>
        <span><svg width="12" height="10"><path d="M1 9 Q2 3 7 3 V0 L12 4.5 L7 9 V6 Q3 6 1 9Z" fill="#555"/></svg>Share</span>
        <span><svg width="16" height="4"><circle cx="2" cy="2" r="2" fill="#555"/><circle cx="8" cy="2" r="2" fill="#555"/><circle cx="14" cy="2" r="2" fill="#555"/></svg>More</span>
        <span class="stat"><svg width="11" height="10"><path d="M0 4h2v6H0zM3 4l3-4c1 0 1.5.7 1.2 2L7 4h3.5l-1 6H3z" fill="#555"/></svg>12.0212</span>
        <span><svg width="11" height="10"><path d="M0 6h2V0H0zM3 6l3 4c1 0 1.5-.7 1.2-2L7 6h3.5l-1-6H3z" fill="#555"/></svg>254</span>
      </div>
    </article>
    <aside class="side-list">
      <div class="side-item"><div class="side-thumb" role="img" aria-label="Hands holding a plant in a garden" style="background:linear-gradient(135deg,#9aa67a,#5b6b3e)"><svg class="play" width="30" height="30" viewBox="0 0 30 30"><circle cx="15" cy="15" r="13" fill="none" stroke="#fff" stroke-width="2"/><path d="M12 9l9 6-9 6z" fill="#fff"/></svg></div><div class="side-text">Nemo enim ipsam voluptatem quia voluptas sit<div class="views">155,836 view</div></div></div>
      <div class="side-item"><div class="side-thumb" role="img" aria-label="Man sitting in front of city buildings" style="background:linear-gradient(135deg,#8ba3c2,#3b4a5e)"><svg class="play" width="30" height="30" viewBox="0 0 30 30"><circle cx="15" cy="15" r="13" fill="none" stroke="#fff" stroke-width="2"/><path d="M12 9l9 6-9 6z" fill="#fff"/></svg></div><div class="side-text">Nemo enim ipsam voluptatem quia voluptas sit<div class="views">155,836 view</div></div></div>
      <div class="side-item"><div class="side-thumb" role="img" aria-label="Car on a road at dusk" style="background:linear-gradient(135deg,#d19a5c,#2d3b4c)"><svg class="play" width="30" height="30" viewBox="0 0 30 30"><circle cx="15" cy="15" r="13" fill="none" stroke="#fff" stroke-width="2"/><path d="M12 9l9 6-9 6z" fill="#fff"/></svg></div><div class="side-text">Nemo enim ipsam voluptatem quia voluptas sit<div class="views">155,836 view</div></div></div>
      <div class="side-item"><div class="side-thumb" role="img" aria-label="Hiker in autumn woods" style="background:linear-gradient(135deg,#a08459,#4c3c2a)"><svg class="play" width="30" height="30" viewBox="0 0 30 30"><circle cx="15" cy="15" r="13" fill="none" stroke="#fff" stroke-width="2"/><path d="M12 9l9 6-9 6z" fill="#fff"/></svg></div><div class="side-text">Nemo enim ipsam voluptatem quia voluptas sit<div class="views">155,836 view</div></div></div>
      <div class="side-item"><div class="side-thumb" role="img" aria-label="Person doing yoga outdoors" style="background:linear-gradient(135deg,#8fa06a,#4d5a38)"><svg class="play" width="30" height="30" viewBox="0 0 30 30"><circle cx="15" cy="15" r="13" fill="none" stroke="#fff" stroke-width="2"/><path d="M12 9l9 6-9 6z" fill="#fff"/></svg></div><div class="side-text">Nemo enim ipsam voluptatem quia voluptas sit<div class="views">155,836 view</div></div></div>
    </aside>
  </div>
</section>

<section class="video-section" style="margin-top:62px">
  <div class="wrap">
    <h2 class="section-title">Recently uploaded</h2>
    <div class="card-row">
      <div class="card"><div class="card-media" role="img" aria-label="Backpacker on a hilltop at sunset" style="background:linear-gradient(160deg,#e0a04a,#5a3a1e)"><svg class="play" width="34" height="34" viewBox="0 0 30 30"><circle cx="15" cy="15" r="13" fill="none" stroke="#fff" stroke-width="2"/><path d="M12 9l9 6-9 6z" fill="#fff"/></svg></div><p class="card-desc">Lorem ipsum dolor sit amet, consectetur adipisicing elit, sed do eiusmod</p><div class="card-meta"><span>276,439 views</span><span>6 hours ago</span></div></div>
      <div class="card"><div class="card-media" role="img" aria-label="Two friends laughing at a phone in a cafe" style="background:linear-gradient(160deg,#b98e6a,#4a3a30)"><svg class="play" width="34" height="34" viewBox="0 0 30 30"><circle cx="15" cy="15" r="13" fill="none" stroke="#fff" stroke-width="2"/><path d="M12 9l9 6-9 6z" fill="#fff"/></svg></div><p class="card-desc">Lorem ipsum dolor sit amet, consectetur adipisicing elit, sed do eiusmod</p><div class="card-meta"><span>276,439 views</span><span>6 hours ago</span></div></div>
      <div class="card"><div class="card-media" role="img" aria-label="Woman riding a bicycle on an old street" style="background:linear-gradient(160deg,#9a9488,#5c564c)"><svg class="play" width="34" height="34" viewBox="0 0 30 30"><circle cx="15" cy="15" r="13" fill="none" stroke="#fff" stroke-width="2"/><path d="M12 9l9 6-9 6z" fill="#fff"/></svg></div><p class="card-desc">Lorem ipsum dolor sit amet, consectetur adipisicing elit, sed do eiusmod</p><div class="card-meta"><span>276,439 views</span><span>6 hours ago</span></div></div>
      <div class="card"><div class="card-media" role="img" aria-label="Hikers crossing a mountain stream" style="background:linear-gradient(160deg,#8ea0a8,#3d4a3c)"><svg class="play" width="34" height="34" viewBox="0 0 30 30"><circle cx="15" cy="15" r="13" fill="none" stroke="#fff" stroke-width="2"/><path d="M12 9l9 6-9 6z" fill="#fff"/></svg></div><p class="card-desc">Lorem ipsum dolor sit amet, consectetur adipisicing elit, sed do eiusmod</p><div class="card-meta"><span>276,439 views</span><span>6 hours ago</span></div></div>
    </div>
  </div>
</section>

<section class="video-section" style="margin-top:69px">
  <div class="wrap">
    <h2 class="section-title">Live Recommendations</h2>
    <div class="card-row">
      <div class="card"><div class="card-media" role="img" aria-label="Horses grazing in a green field" style="background:linear-gradient(180deg,#b8cde0 0%,#7a9a4a 40%,#5d7a34 100%)"><svg class="play" width="34" height="34" viewBox="0 0 30 30"><circle cx="15" cy="15" r="13" fill="none" stroke="#fff" stroke-width="2"/><path d="M12 9l9 6-9 6z" fill="#fff"/></svg></div><p class="card-desc">Lorem ipsum dolor sit amet, consectetur adipisicing elit, sed do eiusmod</p><div class="card-meta"><span>276,439 views</span><span>6 hours ago</span></div></div>
      <div class="card"><div class="card-media" role="img" aria-label="Person in a suit with a cat mask against the sky" style="background:linear-gradient(180deg,#4f8fc8,#a8c8e2)"><svg class="play" width="34" height="34" viewBox="0 0 30 30"><circle cx="15" cy="15" r="13" fill="none" stroke="#fff" stroke-width="2"/><path d="M12 9l9 6-9 6z" fill="#fff"/></svg></div><p class="card-desc">Lorem ipsum dolor sit amet, consectetur adipisicing elit, sed do eiusmod</p><div class="card-meta"><span>276,439 views</span><span>6 hours ago</span></div></div>
      <div class="card"><div class="card-media" role="img" aria-label="Zebras on the savanna at sunset" style="background:linear-gradient(180deg,#f0a030,#c0701e 50%,#6a4a22)"><svg class="play" width="34" height="34" viewBox="0 0 30 30"><circle cx="15" cy="15" r="13" fill="none" stroke="#fff" stroke-width="2"/><path d="M12 9l9 6-9 6z" fill="#fff"/></svg></div><p class="card-desc">Lorem ipsum dolor sit amet, consectetur adipisicing elit, sed do eiusmod</p><div class="card-meta"><span>276,439 views</span><span>6 hours ago</span></div></div>
      <div class="card"><div class="card-media" role="img" aria-label="Sheep grazing on a hillside" style="background:linear-gradient(180deg,#a8c0d8 0%,#6d8f50 45%,#4f7a2e 100%)"><svg class="play" width="34" height="34" viewBox="0 0 30 30"><circle cx="15" cy="15" r="13" fill="none" stroke="#fff" stroke-width="2"/><path d="M12 9l9 6-9 6z" fill="#fff"/></svg></div><p class="card-desc">Lorem ipsum dolor sit amet, consectetur adipisicing elit, sed do eiusmod</p><div class="card-meta"><span>276,439 views</span><span>6 hours ago</span></div></div>
    </div>
  </div>
</section>

<section class="video-section" style="margin-top:69px">
  <div class="wrap">
    <h2 class="section-title">Entertainment</h2>
    <div class="card-row">
      <div class="card"><div class="card-media" role="img" aria-label="Friends dancing at a party with confetti" style="background:linear-gradient(160deg,#c05040,#3a2426)"><svg class="play" width="34" height="34" viewBox="0 0 30 30"><circle cx="15" cy="15" r="13" fill="none" stroke="#fff" stroke-width="2"/><path d="M12 9l9 6-9 6z" fill="#fff"/></svg></div><p class="card-desc">Lorem ipsum dolor sit amet, consectetur adipisicing elit, sed do eiusmod</p><div class="card-meta"><span>276,439 views</span><span>6 hours ago</span></div></div>
      <div class="card"><div class="card-media" role="img" aria-label="Friends playing in a swimming pool" style="background:linear-gradient(160deg,#3aa0c0,#d06088)"><svg class="play" width="34" height="34" viewBox="0 0 30 30"><circle cx="15" cy="15" r="13" fill="none" stroke="#fff" stroke-width="2"/><path d="M12 9l9 6-9 6z" fill="#fff"/></svg></div><p class="card-desc">Lorem ipsum dolor sit amet, consectetur adipisicing elit, sed do eiusmod</p><div class="card-meta"><span>276,439 views</span><span>6 hours ago</span></div></div>
      <div class="card"><div class="card-media" role="img" aria-label="Audience watching a film in a cinema" style="background:linear-gradient(160deg,#4a4038,#151210)"><svg class="play" width="34" height="34" viewBox="0 0 30 30"><circle cx="15" cy="15" r="13" fill="none" stroke="#fff" stroke-width="2"/><path d="M12 9l9 6-9 6z" fill="#fff"/></svg></div><p class="card-desc">Lorem ipsum dolor sit amet, consectetur adipisicing elit, sed do eiusmod</p><div class="card-meta"><span>276,439 views</span><span>6 hours ago</span></div></div>
      <div class="card"><div class="card-media" role="img" aria-label="Bear in a forest beside an old television" style="background:linear-gradient(160deg,#c08a50,#4a3220)"><svg class="play" width="34" height="34" viewBox="0 0 30 30"><circle cx="15" cy="15" r="13" fill="none" stroke="#fff" stroke-width="2"/><path d="M12 9l9 6-9 6z" fill="#fff"/></svg></div><p class="card-desc">Lorem ipsum dolor sit amet, consectetur adipisicing elit, sed do eiusmod</p><div class="card-meta"><span>276,439 views</span><span>6 hours ago</span></div></div>
    </div>
  </div>
</section>

<section class="popular">
  <h2 class="popular-title">MOST POPULAR POSTS</h2>
  <div class="wrap">
    <div class="post-row">
      <article class="post"><div class="post-media" role="img" aria-label="Hands holding a game controller" style="background:linear-gradient(160deg,#e8e4de,#7a8a9a)"><span class="tag">GAMES</span></div><h3 class="post-title">Lorem Ipsum is simply dummy<br>Text of the printing</h3><div class="post-meta"><span><svg width="9" height="8"><path d="M0 0h9v6H3L1 8V6H0z" fill="#fff"/></svg>2 Comments</span><span><svg width="9" height="9"><rect x=".5" y="1.5" width="8" height="7" fill="none" stroke="#fff"/><line x1="0" y1="3.5" x2="9" y2="3.5" stroke="#fff"/></svg>July 11, 2017</span></div></article>
      <article class="post"><div class="post-media" role="img" aria-label="Football players celebrating in a stadium" style="background:linear-gradient(160deg,#6a8aa8,#3a5a2a)"><span class="tag">GAMES</span></div><h3 class="post-title">Lorem Ipsum is simply dummy<br>Text of the printing</h3><div class="post-meta"><span><svg width="9" height="8"><path d="M0 0h9v6H3L1 8V6H0z" fill="#fff"/></svg>2 Comments</span><span><svg width="9" height="9"><rect x=".5" y="1.5" width="8" height="7" fill="none" stroke="#fff"/><line x1="0" y1="3.5" x2="9" y2="3.5" stroke="#fff"/></svg>July 11, 2017</span></div></article>
      <article class="post"><div class="post-media" role="img" aria-label="Young man playing an arcade machine" style="background:linear-gradient(160deg,#3a5ab0,#c03040)"><span class="tag">GAMES</span></div><h3 class="post-title">Lorem Ipsum is simply dummy<br>Text of the printing</h3><div class="post-meta"><span><svg width="9" height="8"><path d="M0 0h9v6H3L1 8V6H0z" fill="#fff"/></svg>2 Comments</span><span><svg width="9" height="9"><rect x=".5" y="1.5" width="8" height="7" fill="none" stroke="#fff"/><line x1="0" y1="3.5" x2="9" y2="3.5" stroke="#fff"/></svg>July 11, 2017</span></div></article>
      <article class="post"><div class="post-media" role="img" aria-label="Excited gamer with a controller and sports players behind" style="background:linear-gradient(160deg,#3a6ab0,#d08a40)"><span class="tag">GAMES</span></div><h3 class="post-title">Lorem Ipsum is simply dummy<br>Text of the printing</h3><div class="post-meta"><span><svg width="9" height="8"><path d="M0 0h9v6H3L1 8V6H0z" fill="#fff"/></svg>2 Comments</span><span><svg width="9" height="9"><rect x=".5" y="1.5" width="8" height="7" fill="none" stroke="#fff"/><line x1="0" y1="3.5" x2="9" y2="3.5" stroke="#fff"/></svg>July 11, 2017</span></div></article>
    </div>
  </div>
</section>

<footer class="site-footer">
  <div class="social" aria-label="Social links">
    <a class="social-link" href="#" aria-label="Social link"><svg width="10" height="10" viewBox="0 0 10 10"><circle cx="5" cy="5" r="3" fill="none" stroke="#fff" stroke-width="1.5"/></svg></a>
    <a class="social-link" href="#" aria-label="Social link"><svg width="10" height="10" viewBox="0 0 10 10"><circle cx="5" cy="5" r="3" fill="none" stroke="#fff" stroke-width="1.5"/></svg></a>
    <a class="social-link" href="#" aria-label="Social link"><svg width="10" height="10" viewBox="0 0 10 10"><circle cx="5" cy="5" r="3" fill="none" stroke="#fff" stroke-width="1.5"/></svg></a>
    <a class="social-link" href="#" aria-label="Social link"><svg width="10" height="10" viewBox="0 0 10 10"><circle cx="5" cy="5" r="3" fill="none" stroke="#fff" stroke-width="1.5"/></svg></a>
    <a class="social-link" href="#" aria-label="Social link"><svg width="10" height="10" viewBox="0 0 10 10"><circle cx="5" cy="5" r="3" fill="none" stroke="#fff" stroke-width="1.5"/></svg></a>
  </div>
  <nav class="foot-nav"><a href="#">Home</a><i>/</i><a href="#">Trending</a><i>/</i><a href="#">Entertainment</a><i>/</i><a href="#">Videos</a><i>/</i><a href="#">Subscriptions</a><i>/</i><a href="#">Contacts</a></nav>
  <p class="copyright">Copyright @ 2017 Fenno Reels. All Rights Reserved.</p>
</footer>

</body>
</html>
```